Wine Label Design

Organization name: Halvern Wine Company

My company is called Halvern Wine Company, I’m a wine importer and wholesaler who distributes wine domestically.

We are about to launch a line of three premium and one sparkling wine that we will wholesale to various retailers, wine stores, and restaurants for re-sale. The wines label will have “Dorian Halvern” I plan on having the labels the same and just changing the varietal as needed. My wine are made from premium grapes and will be marketed as a high end wine. My current label size is 3 1/2" wide by 5" in long and the labels can be on a solid background or transparent.

I would like the first label to be for my Cabernet Sauvignon, California, 2012, 750ML (for the size of the bottle) and ALC 13.8% BY VOL (for the alcohol content).

Colors: I am open to any and all designs that would alter my perception of what will be best!

Further:
Current label is boring and poorly done, so hopefully you designers can come up with something better

Industry/Entity Type

It Company

```html
<!DOCTYPE html>
<html lang="en">
<head>
<meta charset="utf-8">
<title>Dorian Halvern – Cabernet Sauvignon Label</title>
<link rel="stylesheet" href="https://fonts.googleapis.com/css2?family=Cinzel:wght@700&family=Herr+Von+Muellerhoff&family=Parisienne&family=Jost:wght@300&display=swap">
<style>
  :root {
    --label-red: #861722;
    --label-deep: #5a0d15;
    --ornament-dark: #3a0408;
    --gold: #bd9c5d;
    --gold-light: #f3e2a6;
    --pill: #2a0205;
    --white: #ffffff;
  }
  html, body {
    margin: 0;
    padding: 0;
    width: 840px;
    height: 1200px;
    overflow: hidden;
    background: var(--label-red);
  }
  .label {
    position: relative;
    width: 840px;
    height: 1200px;
    background: var(--label-red);
    overflow: hidden;
  }
  .gold-band {
    position: absolute;
    left: 0;
    width: 840px;
    height: 16px;
    background: linear-gradient(90deg, var(--gold), var(--gold-light) 50%, var(--gold));
  }
  .gold-band--top { top: 0; }
  .gold-band--bottom { bottom: 0; }

  .corner-flourish {
    position: absolute;
    width: 300px;
    height: 380px;
  }
  .corner-flourish--tl { top: 16px; left: 0; background: radial-gradient(ellipse at 0% 0%, var(--ornament-dark) 0%, rgba(58,4,8,0.55) 35%, rgba(134,23,34,0) 70%); }
  .corner-flourish--tr { top: 16px; right: 0; background: radial-gradient(ellipse at 100% 0%, var(--ornament-dark) 0%, rgba(58,4,8,0.55) 30%, rgba(134,23,34,0) 65%); }
  .corner-flourish--bl { bottom: 16px; left: 0; background: radial-gradient(ellipse at 0% 100%, var(--ornament-dark) 0%, rgba(58,4,8,0.55) 30%, rgba(134,23,34,0) 65%); }
  .corner-flourish--br { bottom: 16px; right: 0; width: 340px; height: 460px; background: radial-gradient(ellipse at 100% 100%, var(--ornament-dark) 0%, rgba(58,4,8,0.6) 35%, rgba(134,23,34,0) 70%); }

  .brand-name {
    position: absolute;
    top: 96px;
    left: 0;
    width: 840px;
    text-align: center;
    font-family: "Herr Von Muellerhoff", cursive;
    font-size: 150px;
    line-height: 1.2;
    color: var(--gold);
    margin: 0;
    font-weight: 400;
  }
  .scroll-divider {
    position: absolute;
    left: 144px;
    width: 540px;
    height: 26px;
    border-radius: 13px;
    background: linear-gradient(90deg, rgba(42,2,5,0), rgba(42,2,5,0.55) 20%, rgba(42,2,5,0.75) 50%, rgba(42,2,5,0.55) 80%, rgba(42,2,5,0));
  }
  .scroll-divider--upper { top: 380px; }
  .scroll-divider--lower { top: 880px; }

  .varietal {
    position: absolute;
    left: 0;
    width: 840px;
    text-align: center;
    font-family: "Cinzel", serif;
    font-weight: 700;
    color: var(--gold);
    margin: 0;
    line-height: 1;
  }
  .varietal--line1 { top: 424px; font-size: 104px; }
  .varietal--line2 { top: 546px; font-size: 108px; }

  .appellation {
    position: absolute;
    top: 668px;
    left: 0;
    width: 840px;
    text-align: center;
    font-family: "Parisienne", cursive;
    font-size: 62px;
    color: var(--white);
    line-height: 1.2;
  }
  .vintage {
    position: absolute;
    top: 782px;
    left: 324px;
    width: 190px;
    height: 84px;
    border-radius: 50%;
    background: var(--pill);
    color: var(--gold);
    font-family: "Jost", sans-serif;
    font-weight: 300;
    font-size: 56px;
    line-height: 84px;
    text-align: center;
    letter-spacing: 1px;
  }
  .bottle-size, .alcohol {
    position: absolute;
    left: 0;
    width: 840px;
    text-align: center;
    font-family: "Jost", sans-serif;
    font-weight: 300;
    color: var(--white);
    line-height: 1;
  }
  .bottle-size { top: 990px; font-size: 40px; }
  .alcohol { top: 1072px; font-size: 32px; }
</style>
</head>
<body>
<main class="label">
  <div class="gold-band gold-band--top"></div>
  <div class="corner-flourish corner-flourish--tl" role="img" aria-label="Baroque acanthus scroll ornament, top left corner"></div>
  <div class="corner-flourish corner-flourish--tr" role="img" aria-label="Baroque acanthus scroll ornament, top right corner"></div>
  <div class="corner-flourish corner-flourish--bl" role="img" aria-label="Baroque acanthus scroll ornament, bottom left corner"></div>
  <div class="corner-flourish corner-flourish--br" role="img" aria-label="Baroque acanthus scroll ornament, bottom right corner"></div>

  <h1 class="brand-name">Dorian Halvern</h1>
  <div class="scroll-divider scroll-divider--upper" role="img" aria-label="Decorative swirl divider"></div>
  <h2 class="varietal varietal--line1">Cabernet</h2>
  <h2 class="varietal varietal--line2">Sauvignon</h2>
  <div class="appellation">California</div>
  <div class="vintage">2012</div>
  <div class="scroll-divider scroll-divider--lower" role="img" aria-label="Decorative swirl divider"></div>
  <div class="bottle-size">750 ML</div>
  <div class="alcohol">ALC 13.8% BY VOL</div>
  <div class="gold-band gold-band--bottom"></div>
</main>
</body>
</html>
```